Organic Vanu (Coffee) Scrub Label for high end product

Need a product label for a coffee based body scrub called Vanu Body Scrub a 100% organic product. Our primary target is the yoga community so designs should reflect calm, perhaps incorporate eastern yoga symbology. simpler the better. Design should include both a round lid label and a rectangular wrap around label.

yoga community, people with cellulite, etc.

Community

```html
<!DOCTYPE html>
<html lang="en">
<head>
<meta charset="utf-8">
<title>Vanu Scrub – Label Set</title>
<link rel="stylesheet" href="https://fonts.googleapis.com/css2?family=Josefin+Sans:wght@400;600;700&display=swap">
<style>
  :root {
    --page-bg: #ffffff;
    --label-blush: #e9d6d4;
    --ink-brown: #5b2f12;
  }
  html, body {
    margin: 0;
    padding: 0;
    width: 1200px;
    height: 725px;
    overflow: hidden;
    background: var(--page-bg);
  }
  .label-sheet {
    display: block;
    width: 1200px;
    height: 725px;
  }
  .label-sheet text {
    font-family: "Josefin Sans", sans-serif;
    fill: var(--ink-brown);
  }
  .label-fill { fill: var(--label-blush); }
  .rule { stroke: var(--ink-brown); stroke-width: 1.2; fill: none; }
  .brand-title { font-weight: 700; letter-spacing: 2px; }
  .product-line { font-weight: 600; letter-spacing: 1.2px; }
  .claim-line { font-weight: 700; letter-spacing: 1px; }
  .brand-mark { font-weight: 700; letter-spacing: 3px; }
  .mark-dot { fill: none; stroke: var(--ink-brown); stroke-width: 2.5; }
</style>
</head>
<body>
<svg class="label-sheet" viewBox="0 0 1200 725" xmlns="http://www.w3.org/2000/svg">
  <defs>
    <path id="lid-title-arc" d="M78,350 A100,100 0 0 1 278,350"/>
    <path id="lid-subtitle-arc" d="M64,350 A114,114 0 0 0 292,350"/>
  </defs>

  <!-- Round lid label -->
  <g class="lid-label">
    <circle class="label-fill" cx="178" cy="350" r="150"/>
    <path class="rule" d="M55.8,305.5 A130,130 0 1 0 300.2,305.5"/>
    <text class="brand-title" font-size="31">
      <textPath href="#lid-title-arc" startOffset="50%" text-anchor="middle">VANU SCRUB</textPath>
    </text>
    <text class="product-line" font-size="14">
      <textPath href="#lid-subtitle-arc" startOffset="50%" text-anchor="middle">COFFEE BODY SCRUB</textPath>
    </text>
    <g class="brand-mark-group">
      <circle class="mark-dot" cx="132" cy="352" r="10"/>
      <text class="brand-mark" x="188" y="363" font-size="30" text-anchor="middle">VANU</text>
    </g>
  </g>

  <!-- Rectangular wrap label -->
  <g class="wrap-label">
    <rect class="label-fill" x="794" y="173" width="377" height="377"/>
    <g class="brand-mark-group">
      <circle class="mark-dot" cx="916" cy="286" r="13"/>
      <text class="brand-mark" x="994" y="300" font-size="40" text-anchor="middle">VANU</text>
    </g>
    <text class="brand-title" x="982.5" y="426" font-size="44" text-anchor="middle">VANU SCRUB</text>
    <line class="rule" x1="832" y1="442" x2="1132" y2="442"/>
    <text class="product-line" x="982.5" y="466" font-size="17" text-anchor="middle">COFFEE BODY SCRUB</text>
    <line class="rule" x1="832" y1="478" x2="1132" y2="478"/>
    <text class="claim-line" x="982.5" y="500" font-size="11" text-anchor="middle">100% ORGANIC PRODUCT</text>
    <line class="rule" x1="832" y1="516" x2="1132" y2="516"/>
  </g>
</svg>
</body>
</html>
```